Business card for Luxury Portable Restroom Trailer company

We are a Luxury Portable Restroom Trailer Company Called FALVEX HIRINGS. Based in Orange County California. We provide portable restroom trailers for events, such as, Weddings, Concerts, Charity events, Sporting events, Tournaments, Corporate events, ect. We rent and Sell the Luxury restrooms. Our colors are white, grey, and Orange. As you will see in the logo we uploaded.
There are 2 people in the company so the names and titles will change for the 3 people but card will remain the same. Here is the information for each Person: Desmond Purt CFO 555 018-3374
next Person: Milo Fenwright VP 555 018-3374
Next Person: Owen Fenwright CEO 555 018-3374
Information to include on the card: Luxury Restroom Trailers Rental and Sales. Weddings, Concerts, Charity, Sporting and Corp. Events.

```html
<!DOCTYPE html>
<html lang="en">
<head>
<meta charset="utf-8">
<title>Falvex Hirings – Business Card</title>
<link rel="stylesheet" href="https://fonts.googleapis.com/css2?family=Montserrat:wght@500;600;800;900&display=swap">
<style>
  :root {
    --orange: #f26c22;
    --grey: #58585a;
    --white: #ffffff;
    --stage: #2c2c2e;
    --text: #2f2f31;
  }
  * { margin: 0; padding: 0; box-sizing: border-box; }
  html, body {
    width: 1200px; height: 880px; overflow: hidden;
    background: var(--stage);
    font-family: "Montserrat", Arial, sans-serif;
  }
  .card {
    position: absolute; left: 260px;
    width: 680px; height: 388px;
    background: var(--white);
    overflow: hidden;
  }
  .card--front { top: 40px; }
  .card--back { top: 452px; }

  /* Front */
  .brand {
    position: absolute; left: 0; right: 0; top: 92px;
    display: flex; align-items: center; justify-content: center; gap: 18px;
  }
  .brand__square {
    width: 40px; height: 40px; background: var(--orange);
  }
  .brand__name {
    font-weight: 900; font-size: 54px; letter-spacing: 1px;
    color: var(--grey); line-height: 1;
  }
  .services {
    position: absolute; left: 0; right: 0; top: 226px;
    text-align: center; color: var(--text);
    font-weight: 500; font-size: 19px; line-height: 1.7;
  }
  .services li { list-style: none; display: inline; }
  .services li::before {
    content: ""; display: inline-block; width: 10px; height: 10px;
    border-radius: 50%; background: var(--orange);
    margin: 0 7px 2px 12px; vertical-align: middle;
  }
  .services ul { display: block; }

  /* Back */
  .swoosh { position: absolute; left: 0; top: 0; }
  .emblem {
    position: absolute; left: 70px; top: 64px;
    width: 196px; height: 196px; border-radius: 50%;
    border: 12px solid var(--orange);
    display: flex; align-items: center; justify-content: center;
    text-align: center;
  }
  .emblem__name {
    font-weight: 900; font-size: 24px; line-height: 1.15;
    color: var(--orange);
  }
  .divider {
    position: absolute; left: 318px; top: 40px;
    width: 2px; height: 250px; background: var(--orange);
  }
  .team { position: absolute; left: 340px; top: 34px; }
  .member { margin-bottom: 10px; }
  .member__name {
    font-weight: 900; font-size: 21px; color: var(--grey);
    text-transform: uppercase; line-height: 1.1;
  }
  .member__name .last { color: var(--orange); }
  .member__title {
    font-weight: 600; font-size: 15px; color: var(--text); line-height: 1.3;
  }
  .member__phone {
    display: flex; align-items: center; gap: 8px;
    font-weight: 600; font-size: 16px; color: var(--text);
  }
  .member__phone svg { width: 16px; height: 16px; fill: var(--orange); }
</style>
</head>
<body>

<section class="card card--front">
  <div class="brand">
    <span class="brand__square"></span>
    <span class="brand__name">FALVEX HIRINGS</span>
  </div>
  <div class="services">
    <ul><li>Luxury Restroom Trailers Rental and Sales</li></ul>
    <ul>
      <li>Weddings</li><li>Concerts</li><li>Charity</li><li>Sporting and Corp</li><li>Events</li>
    </ul>
  </div>
</section>

<section class="card card--back">
  <svg class="swoosh" width="680" height="388" viewBox="0 0 680 388" aria-hidden="true">
    <path d="M0 388 L0 318 Q360 300 680 178 L680 388 Z" fill="var(--orange)"/>
    <path d="M150 312 Q450 285 660 150 Q470 275 150 318 Z" fill="var(--grey)"/>
  </svg>

  <div class="emblem">
    <span class="emblem__name">FALVEX<br>HIRINGS</span>
  </div>

  <div class="divider"></div>

  <div class="team">
    <div class="member">
      <div class="member__name">Desmond <span class="last">Purt</span></div>
      <div class="member__title">CFO</div>
      <div class="member__phone">
        <svg viewBox="0 0 24 24"><path d="M6.6 10.8a15.1 15.1 0 0 0 6.6 6.6l2.2-2.2a1 1 0 0 1 1-.25 11.4 11.4 0 0 0 3.6.57 1 1 0 0 1 1 1V20a1 1 0 0 1-1 1A17 17 0 0 1 3 4a1 1 0 0 1 1-1h3.5a1 1 0 0 1 1 1c0 1.25.2 2.45.57 3.57a1 1 0 0 1-.25 1z"/></svg>
        555 018-3374
      </div>
    </div>
    <div class="member">
      <div class="member__name">Milo <span class="last">Fenwright</span></div>
      <div class="member__title">VP</div>
      <div class="member__phone">
        <svg viewBox="0 0 24 24"><path d="M6.6 10.8a15.1 15.1 0 0 0 6.6 6.6l2.2-2.2a1 1 0 0 1 1-.25 11.4 11.4 0 0 0 3.6.57 1 1 0 0 1 1 1V20a1 1 0 0 1-1 1A17 17 0 0 1 3 4a1 1 0 0 1 1-1h3.5a1 1 0 0 1 1 1c0 1.25.2 2.45.57 3.57a1 1 0 0 1-.25 1z"/></svg>
        555 018-3374
      </div>
    </div>
    <div class="member">
      <div class="member__name">Owen <span class="last">Fenwright</span></div>
      <div class="member__title">CEO</div>
      <div class="member__phone">
        <svg viewBox="0 0 24 24"><path d="M6.6 10.8a15.1 15.1 0 0 0 6.6 6.6l2.2-2.2a1 1 0 0 1 1-.25 11.4 11.4 0 0 0 3.6.57 1 1 0 0 1 1 1V20a1 1 0 0 1-1 1A17 17 0 0 1 3 4a1 1 0 0 1 1-1h3.5a1 1 0 0 1 1 1c0 1.25.2 2.45.57 3.57a1 1 0 0 1-.25 1z"/></svg>
        555 018-3374
      </div>
    </div>
  </div>
</section>

</body>
</html>
```